Modern Business Card Design Needed for Young Realtor

Information that is going on the card:Marcus Penhall
Broker/Owner
555.013.2967
Marcus@MPenhallHomes.example
www.MPenhallHomes.example

Would also like to include my Instagram Handle somewhere. Probably on the back: the_queencity_realtorMy previous business card is attached, I like that one but would like an updated version and maybe a few design changes

Marcus Penhall
Broker/Owner
555.013.2967
Marcus@MPenhallHomes.example
www.MPenhallHomes.example

• Would also like to include my Instagram Handle somewhere. Probably on the back: the_harborline_agent
• Brantley Osgood or the BO (logo from the previous card.)

```html
<!DOCTYPE html>
<html lang="en">
<head>
<meta charset="utf-8">
<title>Marcus Penhall – Business Card</title>
<link rel="stylesheet" href="https://fonts.googleapis.com/css2?family=Arimo:ital,wght@0,400;1,400&family=Cormorant+Garamond:wght@500&family=Tinos:wght@400&display=swap">
<style>
  :root {
    --page: #ffffff;
    --card-white: #ffffff;
    --brand-red: #ae1f2f;
    --wave-dark: #1f1a17;
    --card-black: #000000;
    --text-light: #ffffff;
    --tagline-grey: #6b6b6b;
    --icon-dark: #2a1a1e;
    --gold-light: #f4e7a8;
    --gold-mid: #d9a520;
    --gold-dark: #b8860b;
    --photo-top: #c9ccc9;
    --photo-bottom: #8a8d8f;
  }
  * { margin: 0; padding: 0; box-sizing: border-box; }
  html, body { width: 1200px; height: 1200px; overflow: hidden; background: var(--page); }
  .canvas { position: relative; width: 1200px; height: 1200px; }

  .card {
    position: absolute;
    left: 368px;
    width: 464px;
    height: 265px;
    border-radius: 18px;
    overflow: hidden;
  }
  .card-front { top: 302px; background: var(--card-white); box-shadow: 0 0 0 0.5px #e4e4e4; }
  .card-back { top: 632px; background: var(--card-black); }

  .front-wave { position: absolute; inset: 0; width: 464px; height: 265px; }

  .agent-photo {
    position: absolute;
    left: 21px; top: 22px;
    width: 95px; height: 116px;
    border-radius: 0 0 12px 12px;
    border: 1px solid #ffffff;
    background: linear-gradient(180deg, var(--photo-top) 0%, #aeb1b2 55%, var(--photo-bottom) 100%);
  }

  .brand-block { position: absolute; right: 38px; top: 42px; text-align: center; }
  .brand-name {
    font-family: "Cormorant Garamond", serif;
    font-weight: 500;
    font-size: 22px;
    letter-spacing: 3.6px;
    color: var(--brand-red);
    white-space: nowrap;
  }
  .brand-tagline {
    margin-top: 3px;
    font-family: "Arimo", sans-serif;
    font-style: italic;
    font-size: 12.5px;
    color: var(--tagline-grey);
    white-space: nowrap;
  }

  .agent-name {
    position: absolute; left: 21px; top: 142px;
    font-family: "Tinos", serif;
    font-size: 18.5px;
    color: var(--text-light);
    white-space: nowrap;
  }
  .agent-title {
    position: absolute; left: 22px; top: 163px;
    font-family: "Arimo", sans-serif;
    font-size: 12.5px;
    color: var(--text-light);
  }

  .contact-list { position: absolute; left: 19px; top: 196px; list-style: none; }
  .contact-item {
    display: flex; align-items: center; gap: 5px;
    height: 17.5px;
    font-family: "Arimo", sans-serif;
    font-size: 12.5px;
    color: var(--text-light);
    white-space: nowrap;
  }
  .contact-icon { width: 13px; height: 13px; flex: none; }

  .social-handle {
    position: absolute; right: 20px; top: 231px;
    display: flex; align-items: center; gap: 6px;
    font-family: "Arimo", sans-serif;
    font-size: 12.5px;
    color: var(--text-light);
  }
  .social-dot { width: 11px; height: 11px; border-radius: 50%; background: var(--text-light); }

  .gold-frame { position: absolute; inset: 0; width: 464px; height: 265px; }
  .back-brand {
    position: absolute; left: 0; right: 0; top: 128px;
    text-align: center;
    font-family: "Cormorant Garamond", serif;
    font-weight: 500;
    font-size: 23px;
    letter-spacing: 4px;
    color: var(--text-light);
    white-space: nowrap;
  }
</style>
</head>
<body>
<div class="canvas">

  <section class="card card-front">
    <svg class="front-wave" viewBox="0 0 464 265" aria-hidden="true">
      <path fill="var(--wave-dark)" d="M0,68 Q20,48 40,44 L116,62 C200,80 260,115 340,115 C400,115 440,90 464,70 L464,265 L0,265 Z"/>
      <path fill="var(--brand-red)" d="M0,88 Q20,66 40,60 L116,76 C200,100 260,130 340,130 C400,130 440,106 464,87 L464,265 L0,265 Z"/>
    </svg>

    <div class="agent-photo" role="img" aria-label="Portrait photo of Marcus Penhall"></div>

    <div class="brand-block">
      <div class="brand-name">MPENHALL HOMES</div>
      <div class="brand-tagline">Westbrook Area Market Center</div>
    </div>

    <h1 class="agent-name">MARCUS PENHALL</h1>
    <p class="agent-title">Broker / Owner</p>

    <ul class="contact-list">
      <li class="contact-item">
        <svg class="contact-icon" viewBox="0 0 14 14" aria-hidden="true">
          <circle cx="7" cy="7" r="7" fill="var(--icon-dark)"/>
          <path d="M4.6,4 Q4,6.5 6,8.6 Q8,10.3 9.8,9.6" stroke="#fff" stroke-width="1.4" fill="none" stroke-linecap="round"/>
        </svg>
        555 013 2967
      </li>
      <li class="contact-item">
        <svg class="contact-icon" viewBox="0 0 14 14" aria-hidden="true">
          <circle cx="7" cy="7" r="7" fill="var(--icon-dark)"/>
          <text x="7" y="9.6" text-anchor="middle" font-family="Arimo, sans-serif" font-size="8" fill="#fff">@</text>
        </svg>
        Marcus@MPenhallHomes.example
      </li>
      <li class="contact-item">
        <svg class="contact-icon" viewBox="0 0 14 14" aria-hidden="true">
          <circle cx="7" cy="7" r="7" fill="var(--icon-dark)"/>
          <g stroke="#fff" stroke-width="0.7" fill="none">
            <circle cx="7" cy="7" r="3.8"/>
            <ellipse cx="7" cy="7" rx="1.7" ry="3.8"/>
            <line x1="3.2" y1="7" x2="10.8" y2="7"/>
          </g>
        </svg>
        www.MPenhallHomes.example
      </li>
    </ul>

    <div class="social-handle">
      <span class="social-dot" aria-hidden="true"></span>
      <span>the_harborline_agent</span>
    </div>
  </section>

  <section class="card card-back">
    <svg class="gold-frame" viewBox="0 0 464 265" aria-hidden="true">
      <defs>
        <linearGradient id="goldStroke" x1="0" y1="0" x2="1" y2="1">
          <stop offset="0" stop-color="var(--gold-dark)"/>
          <stop offset="0.3" stop-color="var(--gold-light)"/>
          <stop offset="0.55" stop-color="var(--gold-mid)"/>
          <stop offset="0.8" stop-color="var(--gold-light)"/>
          <stop offset="1" stop-color="var(--gold-dark)"/>
        </linearGradient>
      </defs>
      <rect x="19.5" y="18.5" width="425" height="227" rx="12" fill="none" stroke="url(#goldStroke)" stroke-width="2"/>
    </svg>
    <div class="back-brand">MPENHALL HOMES</div>
  </section>

</div>
</body>
</html>
```